Kerris Odlen Letter Head

log and letter head

would like a modern feminine approch, please see attached the back of my business card

Kerris Odlen Consulting

ABN 81 540 263 918

Address19a Brood Street Marlow Heights 5082 South Australia

Business

```html
<!DOCTYPE html>
<html lang="en">
<head>
<meta charset="utf-8">
<title>Kerris Odlen Consulting — Letterhead</title>
<link rel="stylesheet" href="https://fonts.googleapis.com/css2?family=Source+Sans+3:wght@400&display=swap">
<style>
  :root {
    --backdrop: #eceeed;
    --paper: #ffffff;
    --brand-red: #ff0020;
    --brand-red-deep: #b3001a;
    --charcoal: #333333;
    --ink: #111111;
    --edge: #5a5a5a;
  }
  * { margin: 0; padding: 0; box-sizing: border-box; }
  html, body {
    width: 1000px; height: 1200px; overflow: hidden;
    background: var(--backdrop);
    font-family: "Source Sans 3", "Myriad Pro", Arial, sans-serif;
    color: var(--ink);
  }
  .letterhead {
    position: absolute; left: 184px; top: 205px;
    width: 612px; height: 793px;
    background: var(--paper);
    border: 1px solid var(--edge);
    overflow: hidden;
  }
  .header-band { position: absolute; left: 0; top: 0; width: 612px; height: 144px; display: block; }
  .brand-name {
    position: absolute; left: 33px; top: 11px;
    color: var(--paper); font-weight: 400;
    font-size: 30px; line-height: 1;
  }
  .brand-sub {
    position: absolute; left: 84px; top: 45px;
    color: var(--paper); font-weight: 400;
    font-size: 7px; letter-spacing: 5.5px;
  }
  .company-details {
    position: absolute; left: 34px; top: 66px;
    font-size: 15px; line-height: 16px; color: var(--ink);
  }
  .letter-body {
    position: absolute; left: 75px; top: 199px; width: 520px;
    font-size: 16px; line-height: 19px;
  }
  .letter-body p { white-space: nowrap; }
  .recipient { margin-bottom: 35px; }
  .paragraph-one { margin-bottom: 91px; }
  .paragraph-two { margin-bottom: 55px; }
  .footer-band { position: absolute; left: 0; bottom: 0; width: 612px; height: 10px; display: block; }
</style>
</head>
<body>
  <main class="letterhead">
    <svg class="header-band" viewBox="0 0 612 144" aria-hidden="true">
      <defs>
        <linearGradient id="square-shade" x1="0" y1="0" x2="1" y2="1">
          <stop offset="0" stop-color="var(--brand-red-deep)"/>
          <stop offset="1" stop-color="var(--brand-red)"/>
        </linearGradient>
      </defs>
      <rect width="612" height="144" fill="var(--brand-red)"/>
      <path d="M426,0 C365,6 325,40 305,78 C285,118 240,138 186,144 L612,144 L612,0 Z" fill="var(--charcoal)"/>
      <rect x="541" y="0" width="32" height="32" fill="var(--brand-red)"/>
      <rect x="579" y="0" width="33" height="32" fill="url(#square-shade)"/>
      <rect x="579" y="39" width="33" height="32" fill="var(--brand-red)"/>
    </svg>

    <div class="brand-name">Kerris Odlen</div>
    <div class="brand-sub">CONSULTING</div>

    <div class="company-details">
      <p>ABN 81 540 263 918</p>
      <p>27c Tallow Lane Marlow Heights 5082</p>
      <p>South Australia</p>
    </div>

    <section class="letter-body">
      <div class="recipient">
        <p>To</p>
        <p>jgfjgidfgjijgifdjgij</p>
        <p>chvuxhcvzuxzhuhczxc</p>
        <p>xjchhgydsb</p>
      </div>
      <div class="paragraph-one">
        <p>jvjcxivvvvjjviv hzschuxzc huxc cuhjud ucx cxzcui czxucx cxucu xzxuhcu7</p>
        <p>yhwduuuuuuuuuuuuuuuuxcjhu fidifijfidfjdoifjdifjdiffffffffffffffdosjif f&nbsp;&nbsp;&nbsp;&nbsp; sdusda</p>
        <p>uisduisdusdushcuxucxuyufdjzcfvuxhvzuh dxhgcytruewahf fzxuyvczxvjciju</p>
        <p>xivvxcy7fd uhvcuy7fd&nbsp; y7uf syd7 yy7xc7 wd7ysf7cxuzcut6sdfguwe8rushgdx</p>
        <p>uyhudfvuf vcivu8xcvuxcvicxubbj8u8u8uv8bcxj</p>
      </div>
      <div class="paragraph-two">
        <p>kicjvixuv8xcuvuj&nbsp; x u8u89u9gxjixcuujijgfidxug8x d y87fu8sd u8fdsjxiv</p>
        <p>u8u8fd uy8vucx8u8fd fuc8uv8gflkvcxivkocxvi9civbcxi.</p>
      </div>
      <div class="sign-off">
        <p>gkodfig9fdig</p>
        <p>gvjxfcivjixckvoxc</p>
        <p>cxivjkcxv</p>
      </div>
    </section>

    <svg class="footer-band" viewBox="0 0 612 10" preserveAspectRatio="none" aria-hidden="true">
      <rect width="612" height="10" fill="var(--brand-red)"/>
      <path d="M300,10 C380,4 470,1 612,0 L612,10 Z" fill="var(--charcoal)"/>
    </svg>
  </main>
</body>
</html>
```